Buchcover-Design für Fantasy-Serie
Inspirierte und saubere Umsetzung, sowie kundenorientiert auch bei Sonderwünschen.
Zielgruppe
Buchverlag (Kleinstverlag). Wir verlegen Bücher aus den Genres Fantasy / SciFi / Thriller und Kriminalroman, sowie spezielle thematische Ausgaben. Kern unserer Tätigkeit ist die Wiederveröffentlichung der Nebelhorn-Chronik des deutschen Fantasy Autors Konrad Tilling sowie eine SciFi Serie des deutschen Autor Enno Braxmeyer. Wir suchen genretypische Cover mit Whow-Effekt.
Aufgabenstellung
Bei unserem ersten Auftrag handelt es sich um eine Fantasy Serie, bestehend aus 8 Bänden, welche vorwiegend als Kindle / eBook aber auch als Paperback veröffentlicht werden. Das Titelmotiv stammt jedes Mal von Laurent Dubelcq (lizensiert) und ändert sich bei jedem Buch. Der Titel muss daher von uns bearbeitbar sein.
das EBook hat die üblichen Maße: 1600x2560, 72 dpi
Print wird voraussichtl. 12x19, aber wir benötigen nur den Titel in 300 DPI (identisch mit Ebook lediglich höhere Auflösung).
Text:
(Autorenname): Konrad Tilling
(Buchtitel): Der Zirkel von Quasmar
(Titelzusatz): Erster Roman der Nebelhorn-Chronik
(Gattung): Roman
(Verlagslogo): Wahlweise kleines oder großes Logo, farblich angepasst
Hinweis: bei Auftrag wird das Titelbild in hoher Auflösung von uns geliefert.

```html
<!DOCTYPE html>
<html lang="de">
<head>
<meta charset="utf-8">
<title>Der Zirkel von Quasmar – Buchumschlag</title>
<link rel="stylesheet" href="https://fonts.googleapis.com/css2?family=Tenor+Sans&family=Oswald:wght@400;600&family=Zilla+Slab:wght@600&family=Literata:wght@400&display=swap">
<style>
  :root{
    --page-top:#0d2f4c;
    --page-bottom:#0a1322;
    --band:#0b3b5e;
    --band-soft:rgba(11,59,94,.88);
    --accent:#1ba6ea;
    --white:#ffffff;
    --line:rgba(255,255,255,.7);
    --sky-light:#9fb3c6;
    --sky-mid:#4f6c8c;
    --sky-dark:#1c2f4b;
    --rock-dark:#101c2c;
    --snow:#c9d6e2;
    --label-bg:#2a3d52;
  }
  *{margin:0;padding:0;box-sizing:border-box}
  html,body{width:1200px;height:1200px;overflow:hidden}
  body{
    background:radial-gradient(ellipse at 50% 15%,var(--page-top) 0%,#0b2038 55%,var(--page-bottom) 100%);
    position:relative;
    font-family:"Tenor Sans",sans-serif;
  }
  .cover-spread{
    position:absolute;left:126px;top:246px;width:948px;height:706px;
    box-shadow:0 20px 40px rgba(0,0,0,.6);
    overflow:hidden;
  }
  /* back cover */
  .back-cover{position:absolute;left:0;top:0;width:444px;height:706px}
  .back-art{
    position:absolute;inset:0;
    background:
      radial-gradient(ellipse at 70% 25%,rgba(190,205,220,.55),transparent 45%),
      linear-gradient(180deg,var(--sky-dark) 0%,var(--sky-mid) 35%,var(--sky-light) 52%,#5f7890 68%,#2f4a4a 85%,#1e3534 100%);
  }
  .publisher-name{
    position:absolute;color:var(--white);font-family:"Tenor Sans",sans-serif;
    letter-spacing:.08em;text-align:center;line-height:1;
  }
  .back-cover .publisher-name{left:0;width:444px;top:198px;font-size:24px}
  .blurb-box{
    position:absolute;left:101px;top:242px;width:269px;height:263px;
    background:var(--band-soft);border:1px solid rgba(255,255,255,.35);
    padding:20px 18px;color:var(--white);overflow:hidden;
    font-family:"Literata",serif;font-size:8.6px;line-height:12.4px;text-align:justify;hyphens:auto;
  }
  .blurb-box p + p{margin-top:12px}

  /* spine */
  .spine{
    position:absolute;left:444px;top:0;width:60px;height:706px;background:var(--band);
    border-left:1px solid rgba(255,255,255,.35);border-right:1px solid rgba(255,255,255,.35);
  }
  .spine-title{
    position:absolute;left:16px;top:54px;writing-mode:vertical-rl;
    font-size:25px;letter-spacing:.09em;color:var(--white);white-space:nowrap;
  }
  .spine-title .accent{color:var(--accent)}
  .spine-author{
    position:absolute;left:14px;top:560px;width:30px;height:118px;border:1px solid var(--line);
    writing-mode:vertical-rl;display:flex;align-items:center;justify-content:center;gap:3px;
    white-space:nowrap;
  }
  .spine-author .label{font-family:"Oswald",sans-serif;color:var(--accent);font-size:8px;letter-spacing:.12em;line-height:1}
  .spine-author .name{font-family:"Zilla Slab",serif;font-weight:600;color:var(--white);font-size:9.5px;letter-spacing:.1em;line-height:1}

  /* front cover */
  .front-cover{position:absolute;left:504px;top:0;width:444px;height:706px}
  .front-art{
    position:absolute;inset:0;
    background:
      radial-gradient(ellipse at 70% 80%,var(--snow) 0%,rgba(120,140,160,.6) 22%,transparent 45%),
      radial-gradient(ellipse at 40% 0%,rgba(120,140,160,.6),transparent 35%),
      linear-gradient(180deg,#2c3e55 0%,var(--rock-dark) 40%,#1a2a3c 70%,#24384e 100%);
  }
  .front-cover .publisher-name{left:0;width:444px;top:76px;font-size:36px}
  .title-line{position:absolute;left:0;width:444px;text-align:center;line-height:1;color:var(--white);white-space:nowrap}
  .title-top{top:162px;font-size:50px}
  .title-band{position:absolute;left:0;top:203px;width:444px;height:47px;background:var(--band-soft)}
  .title-main{top:205px;font-size:50px;letter-spacing:-.01em}
  .title-accent{top:255px;font-size:40px;color:var(--accent)}
  .series-panel{position:absolute;left:106px;top:302px;width:232px;height:196px}
  .series-text{position:absolute;left:106px;top:302px;width:232px;text-align:center;color:var(--white)}
  .series-intro{margin-top:54px;font-family:"Oswald",sans-serif;font-size:17px;line-height:1}
  .series-name{margin-top:9px;font-family:"Oswald",sans-serif;font-weight:600;font-size:24px;letter-spacing:.16em;line-height:1}
  .series-suffix{margin-top:6px;font-family:"Oswald",sans-serif;font-weight:600;font-size:24px;color:var(--accent);line-height:1}
  .author-box{
    position:absolute;left:125px;top:615px;width:201px;height:41px;border:1px solid var(--line);
    display:flex;align-items:center;justify-content:center;
  }
  .author-box .label{
    position:absolute;top:-10px;left:50%;transform:translateX(-50%);padding:0 5px;
    font-family:"Oswald",sans-serif;font-size:15px;color:var(--accent);letter-spacing:.1em;
    background:var(--label-bg);line-height:1.2;
  }
  .author-box .name{font-family:"Zilla Slab",serif;font-weight:600;font-size:17px;color:var(--white);letter-spacing:.14em;margin-top:6px;white-space:nowrap}
</style>
</head>
<body>
  <div class="cover-spread">
    <section class="back-cover">
      <div class="back-art" role="img" aria-label="Gemälde: stürmischer Wolkenhimmel über verschneiten Bergwäldern"></div>
      <div class="publisher-name">VELMORA</div>
      <div class="blurb-box">
        <p>Lorem ipsum dolor sit amet, consectetuer adipiscing elit, sed diam nonummy nibh euismod tincidunt ut laoreet dolore magna aliquam erat volutpat. Ut wisi enim ad minim veniam, quis nostrud exerci tation ullamcorper suscipit lobortis nisl ut aliquip ex ea commodo consequat. Duis autem vel eum iriure dolor in hendrerit in vulputate velit esse molestie consequat, vel illum dolore eu feugiat nulla facili</p>
        <p>Lorem ipsum dolor sit amet, consectetuer adipiscing elit, sed diam nonummy nibh euismod tincidunt ut laoreet dolore magna aliquam erat volutpat. Ut wisi enim ad minim veniam, quis nostrud exerci tation ullamcorper suscipit lobortis nisl ut aliquip ex ea commodo consequat. Duis autem vel eum iriure dolor in hendrerit in vulputate velit esse molestie consequat, vel illum dolore eu feugiat nulla facili</p>
      </div>
    </section>

    <section class="spine">
      <div class="spine-title">DER ZIRKEL <span class="accent">VON QUASMAR</span></div>
      <div class="spine-author"><span class="label">Author</span><span class="name">Konrad Tilling</span></div>
    </section>

    <section class="front-cover">
      <div class="front-art" role="img" aria-label="Gemälde: riesige dunkle Felsgestalt über einem verschneiten Hochplateau mit Tannen und einer kleinen Wanderfigur"></div>
      <div class="publisher-name">VELMORA</div>
      <div class="title-band"></div>
      <div class="title-line title-top">DER</div>
      <div class="title-line title-main">ZIRKEL</div>
      <div class="title-line title-accent">VON QUASMAR</div>
      <svg class="series-panel" viewBox="0 0 232 196" aria-hidden="true">
        <path d="M0 0 H232 V196 Q116 152 0 196 Z" fill="#0b3b5e"/>
      </svg>
      <div class="series-text">
        <div class="series-intro">Erster Roman der</div>
        <div class="series-name">Nebelhorn</div>
        <div class="series-suffix">-Chronik</div>
      </div>
      <div class="author-box"><span class="label">Author</span><span class="name">Konrad Tilling</span></div>
    </section>
  </div>
</body>
</html>
```